Bluecrest Wellness Group Website

Need a informative, detailed and functional website for a medical cannabis clinic website

check out www.dumelvaclinic.com as competition - want better site than they have

Target Market(s)

Patients

Industry/Entity Type

Health Care

Number of Pages Required

1 page

Font styles to use
Sans Serif

Colors
cadf82
abd036
9bcb3b
3276b5
33a6d7
0392cd
f68d4e

Requirements
Must have
• Clean / Informative
• Will add additional educational content on opioid reduction
Nice to have
• like the white contrast with black/slate dividers. Green logo looks good on slate
• Check documents for ppt regarding website ideas
Should not have
• too many words

```html
<!DOCTYPE html>
<html lang="en">
<head>
<meta charset="utf-8">
<title>Bluecrest Wellness Group</title>
<link href="https://fonts.googleapis.com/css2?family=Montserrat:wght@400;500;600;700&family=Open+Sans:wght@400;600;700&display=swap" rel="stylesheet">
<style>
:root{
  --lime:#cadf82;
  --leaf:#abd036;
  --leaf-dark:#8cbf2e;
  --grass:#3d8d3f;
  --blue:#3276b5;
  --sky:#33a6d7;
  --ocean:#0392cd;
  --orange:#f68d4e;
  --ink:#3a3a3a;
  --white:#fff;
}
*{box-sizing:border-box;margin:0;padding:0}
html,body{width:1200px;height:3409px;overflow:hidden}
body{font-family:"Open Sans",Arial,sans-serif;color:var(--ink);background:var(--white);position:relative}
.section{position:absolute;left:0;width:1200px}
h2,h3{font-family:"Montserrat",Arial,sans-serif;font-weight:500}

/* top navigation */
.topnav{top:0;height:20px;background:var(--lime)}
.topnav ul{list-style:none;display:flex;justify-content:flex-end;gap:30px;padding-right:14px;height:20px;align-items:center}
.topnav a{font-family:"Montserrat",sans-serif;font-size:12px;color:#2f3a1d;text-decoration:none;font-weight:500}
.infobar{top:20px;height:71px;background:var(--grass)}
.infobar .welcome{position:absolute;left:320px;top:32px;color:#fff;font-size:13px}
.infobar .help{position:absolute;left:744px;top:14px;color:#fff;font-size:12px;line-height:1.1}
.infobar .help strong{display:block;font-family:"Montserrat",sans-serif;font-size:24px;font-weight:600}
.infobar .mail{position:absolute;left:960px;top:28px;color:#fff;font-size:13px;display:flex;align-items:center;gap:10px}
.brand{position:absolute;left:40px;top:-40px;width:220px;height:220px;border-radius:50%;background:#fff;z-index:5;display:flex;align-items:center;justify-content:center;box-shadow:0 2px 10px rgba(0,0,0,.15)}
.brand span{font-family:"Montserrat",sans-serif;font-weight:600;color:var(--grass);font-size:21px;line-height:1.15;text-align:center;margin-top:40px;letter-spacing:.5px}

/* hero */
.hero{top:91px;height:484px}
.hero .photo{position:absolute;inset:0;background:linear-gradient(110deg,#1f4f46 0%,#3e7d72 35%,#5a8e86 60%,#2f4f4e 100%)}
.hero h1{position:absolute;left:110px;top:200px;font-family:"Montserrat",sans-serif;font-weight:600;font-size:35px;color:#fff;letter-spacing:.5px}
.dots{position:absolute;left:578px;top:455px;display:flex;gap:8px}
.dots i{width:9px;height:9px;border-radius:50%;background:#fff;display:block;opacity:.8}
.dots i:first-child{opacity:1;background:var(--leaf)}
.appoint{position:absolute;left:882px;top:50px;width:300px;height:393px;background:rgba(50,118,181,.82);padding:22px 24px}
.appoint h3{color:#fff;font-size:16px;font-weight:700;display:flex;align-items:center;gap:10px;margin-bottom:22px}
.appoint label{display:block;color:#fff;font-size:11px;font-weight:700;margin:12px 0 5px}
.appoint .field{height:36px;border:1px solid rgba(255,255,255,.7);color:#fff;font-size:11px;padding:9px 10px}
.appoint .field.tall{height:86px}
.appoint .submit{position:absolute;left:98px;top:336px;width:110px;height:28px;background:var(--leaf);color:#fff;font-size:11px;font-weight:700;text-align:center;line-height:28px}

/* services */
.services{top:575px;height:416px}
.services .photo{position:absolute;left:0;top:0;width:614px;height:416px;background:linear-gradient(90deg,#d9a98f 0%,#eccdc1 55%,#fff 100%)}
.services h2{position:absolute;left:527px;top:40px;font-size:30px;color:var(--leaf-dark);font-weight:400}
.rule{display:block;width:40px;height:2px;background:var(--orange)}
.services .rule{position:absolute;left:527px;top:90px}
.services p{position:absolute;left:527px;width:560px;font-size:13px;line-height:23px;color:#555}
.btn-outline{position:absolute;height:38px;border:1px solid var(--orange);color:var(--orange);font-size:12px;font-weight:600;text-align:center;line-height:36px;background:#fff}
.services .call{position:absolute;left:692px;top:313px;color:var(--leaf-dark);font-size:16px}
.services .call strong{color:var(--blue);font-family:"Montserrat",sans-serif;font-size:25px;font-weight:600;margin-left:4px}

/* features */
.features{top:1034px;height:210px}
.feature .circle{position:absolute;width:196px;height:196px;border-radius:50%;background:linear-gradient(180deg,#bfa07c 0%,#e5dbcf 55%,#a2683c 100%)}
.feature .label{position:absolute;background:#fff;padding:4px 10px;font-family:"Montserrat",sans-serif;font-size:20px;color:var(--leaf-dark);border-left:2px solid var(--leaf-dark)}
.feature p{position:absolute;width:220px;font-size:13px;line-height:23px;color:#555}
.feature a{position:absolute;font-size:11px;font-weight:700;color:#333;text-decoration:underline}

/* opioid */
.opioid{top:1287px;height:379px}
.opioid .photo{position:absolute;left:0;top:0;width:700px;height:379px;background:linear-gradient(90deg,#8a9aa6 0%,#c9c5c2 45%,#9cb1c4 100%)}
.opioid .panel{position:absolute;left:460px;top:0;width:740px;height:379px;background:linear-gradient(90deg,rgba(50,118,181,0) 0%,rgba(50,118,181,.92) 22%,var(--blue) 60%,#2f6fb0 100%)}
.opioid h2{position:absolute;left:609px;top:50px;color:#fff;font-size:30px;font-weight:400;letter-spacing:.5px}
.opioid p{position:absolute;left:609px;width:470px;color:#e6f0fa;font-size:13px;line-height:23px}
.opioid .btn{position:absolute;left:609px;top:272px;width:132px;height:38px;border:1px solid #fff;color:#fff;font-size:12px;font-weight:600;text-align:center;line-height:36px}

/* specialists */
.team{top:1666px;height:368px}
.team h2{position:absolute;left:0;width:1200px;text-align:center;top:44px;font-size:29px;color:var(--leaf-dark);font-weight:400}
.member{position:absolute;top:123px;width:196px;text-align:center}
.member .circle{width:196px;height:196px;border-radius:50%;background:linear-gradient(180deg,#dfe9f0 0%,#58a6d6 100%);margin-bottom:-48px}
.member .tag{position:relative;display:inline-block;background:#fff;padding:4px 18px 2px;border-radius:4px}
.member .name{font-family:"Montserrat",sans-serif;font-weight:600;color:var(--grass);font-size:16px}
.member .role{font-size:11px;color:#555}

/* faq */
.faq{top:2034px;height:394px;background:#eef1f2}
.faq .photo{position:absolute;left:516px;top:0;width:684px;height:394px;background:linear-gradient(90deg,#e0e4e5 0%,#d5c0ae 30%,#f2f2f2 65%,#e7ecee 100%)}
.faq h2{position:absolute;left:142px;top:85px;font-size:28px;color:var(--grass);font-weight:400}
.faq p{position:absolute;left:142px;top:150px;width:340px;font-size:15px;line-height:28px;font-weight:600;color:#555}

/* news */
.news{top:2428px;height:372px}
.news h2{position:absolute;left:0;width:1200px;text-align:center;top:50px;font-size:29px;color:var(--leaf-dark);font-weight:400}
.card{position:absolute;top:113px;width:309px;height:207px}
.card .photo{position:absolute;left:0;top:0;width:309px;height:152px;background:linear-gradient(180deg,#c7b8a6 0%,#eee6dc 60%,#b78e6b 100%)}
.card .title{position:absolute;left:0;bottom:0;width:309px;height:55px;background:var(--blue);color:#fff;font-family:"Montserrat",sans-serif;font-size:14px;font-weight:600;line-height:19px;padding:9px 12px}
.card.featured{background:#6f8d2c}
.card.featured .ring{position:absolute;left:134px;top:18px;width:42px;height:42px;border:2px solid rgba(255,255,255,.7);border-radius:50%}
.card.featured .meta{position:absolute;left:12px;top:78px;color:#fff;font-size:10px}
.card.featured .ftitle{position:absolute;left:12px;top:98px;width:285px;color:#fff;font-family:"Montserrat",sans-serif;font-size:15px;font-weight:700;line-height:20px}
.card.featured .excerpt{position:absolute;left:12px;top:146px;width:285px;color:#eef5dc;font-size:10px}

/* newsletter */
.newsletter{top:2800px;height:239px;background:linear-gradient(90deg,#2f6fb0,var(--blue) 50%,#3a7fc0)}
.newsletter h2{position:absolute;left:0;width:1200px;text-align:center;top:40px;color:#fff;font-size:29px;font-weight:400;letter-spacing:1px}
.newsletter .sub{position:absolute;left:0;width:1200px;text-align:center;top:88px;color:#e6f0fa;font-size:14px}
.newsletter .input{position:absolute;top:160px;width:310px;height:38px;border:1px solid rgba(255,255,255,.7);color:#fff;font-size:11px;padding:11px 10px}
.newsletter .send{position:absolute;left:816px;top:160px;width:236px;height:40px;background:var(--orange);color:#fff;font-size:13px;text-align:center;line-height:40px}

/* footer */
.footer{top:3039px;height:370px;background:var(--grass)}
.footer .fbrand{position:absolute;left:114px;top:45px;font-family:"Montserrat",sans-serif;font-weight:600;color:#fff;font-size:19px;line-height:1.2;display:flex;align-items:center;gap:14px}
.footer .fbrand i{width:52px;height:52px;border-radius:50%;background:var(--leaf);display:block}
.footer .about{position:absolute;left:114px;width:300px;color:#fff;font-size:12px;line-height:20px}
.footer h4{position:absolute;top:50px;font-family:"Montserrat",sans-serif;font-size:12px;font-weight:700;color:#fff;letter-spacing:.5px}
.footer h4::after{content:"";display:block;width:24px;height:2px;background:var(--leaf);margin-top:6px}
.footer ul{position:absolute;top:88px;list-style:none}
.footer li{color:#fff;font-size:12px;line-height:27px}
.footer .social li{display:flex;align-items:center;gap:10px}
.footer .social li::before{content:"";width:6px;height:6px;border-radius:50%;background:#fff}
.footer .copy{position:absolute;left:0;width:1200px;text-align:center;top:312px;color:#e3efe3;font-size:11px}
</style>
</head>
<body>

<nav class="section topnav">
  <ul>
    <li><a href="#">HOME</a></li><li><a href="#">ABOUT</a></li><li><a href="#">APPOINMENT</a></li>
    <li><a href="#">OPIOID REDUCTION</a></li><li><a href="#">FAQ</a></li><li><a href="#">BLOG</a></li><li><a href="#">CONTACT</a></li>
  </ul>
</nav>

<header class="section infobar">
  <div class="brand"><span>BLUECREST<br>WELLNESS<br>GROUP</span></div>
  <div class="welcome">Welcome to bluecrest wellness group</div>
  <div class="help">Need help? Call<strong>+00 222 480 36</strong></div>
  <div class="mail">
    <svg width="28" height="20" viewBox="0 0 28 20"><rect x="1" y="1" width="26" height="18" fill="none" stroke="#fff" stroke-width="2"/><path d="M1 1l13 10L27 1" fill="none" stroke="#fff" stroke-width="2"/></svg>
    info@bluecrestwellness.com
  </div>
</header>

<section class="section hero">
  <div class="photo" role="img" aria-label="Surgical team working in a hospital operating room"></div>
  <h1>ADVANCED MEDICINE, TRUSTED CARE</h1>
  <div class="dots"><i></i><i></i><i></i><i></i></div>
  <form class="appoint">
    <h3>
      <svg width="22" height="22" viewBox="0 0 22 22"><path d="M4 2v7a5 5 0 0010 0V2M9 14v3a4 4 0 008 0v-3" fill="none" stroke="#fff" stroke-width="2"/><circle cx="17" cy="12" r="2.5" fill="none" stroke="#fff" stroke-width="2"/></svg>
      MAKE AN APPOINMENT
    </h3>
    <label>NAME</label><div class="field">Enter Name</div>
    <label>EMAIL</label><div class="field">Enter Email</div>
    <label>MESSAGE</label><div class="field tall">Enter Message</div>
    <div class="submit">SUBMIT</div>
  </form>
</section>

<section class="section services">
  <div class="photo" role="img" aria-label="Smiling family of parents holding their baby"></div>
  <h2>Our patient Services</h2>
  <span class="rule"></span>
  <p style="top:110px">Lorem ipsum dolor sit amet, consectetur adipiscing elit. Ut diam justo, ultricies at purus quis, ultricies ornare orci. Integer laoreet finibus mi. Pellentesque tincidunt eget libero vitae pellentesque. Aliquam interdum risus sed neque molestie, sit amet venenatis nisi</p>
  <p style="top:222px">Lorem ipsum dolor sit amet, consectetur adipiscing elit. Ut diam justo, ultricies at purus quis, ultricies ornare orci.</p>
  <div class="btn-outline" style="left:532px;top:312px;width:132px">Read More</div>
  <div class="call">To book an appoinment call <strong>+00 222 480 36</strong></div>
</section>

<section class="section features">
  <div class="feature">
    <div class="circle" role="img" aria-label="Senior couple sitting together at home" style="left:130px;top:5px"></div>
    <div class="label" style="left:120px;top:124px">WHAT WE DO</div>
    <p style="left:362px;top:36px">Aenean velit sem, congue sed ullamcorper vel, cursus eu orci. Aenean nec orci eget velit rhoncus auctor at sit amet nisi.</p>
    <a style="left:362px;top:145px">Read More</a>
  </div>
  <div class="feature">
    <div class="circle" role="img" aria-label="Senior couple sitting together at home" style="left:632px;top:5px"></div>
    <div class="label" style="left:622px;top:124px">WHY CHOOSE US</div>
    <p style="left:865px;top:36px">Aenean velit sem, congue sed ullamcorper vel, cursus eu orci. Aenean nec orci eget velit rhoncus auctor at sit amet nisi.</p>
    <a style="left:865px;top:145px">Read More</a>
  </div>
</section>

<section class="section opioid">
  <div class="photo" role="img" aria-label="Patient resting in a hospital bed"></div>
  <div class="panel"></div>
  <h2>OPIOID REDUCTION</h2>
  <p style="top:118px">Lorem ipsum dolor sit amet, consectetur adipiscing elit. Ut diam justo, ultricies at purus quis, ultricies ornare orci integer laoreet.</p>
  <p style="top:188px">Finibus mi. Pellentesque tincidunt eget libero vitae pellentesque aliquam interdum risus sed neque molestie.</p>
  <div class="btn">Read More</div>
</section>

<section class="section team">
  <h2>MEET WITH OUR SPECIALIST</h2>
  <div class="member" style="left:130px"><div class="circle" role="img" aria-label="Portrait of a senior consultant"></div><div class="tag"><div class="name">John Doe</div><div class="role">Senior Consultant</div></div></div>
  <div class="member" style="left:378px"><div class="circle" role="img" aria-label="Portrait of a senior consultant"></div><div class="tag"><div class="name">John Doe</div><div class="role">Senior Consultant</div></div></div>
  <div class="member" style="left:626px"><div class="circle" role="img" aria-label="Portrait of a senior consultant"></div><div class="tag"><div class="name">John Doe</div><div class="role">Senior Consultant</div></div></div>
  <div class="member" style="left:874px"><div class="circle" role="img" aria-label="Portrait of a senior consultant"></div><div class="tag"><div class="name">John Doe</div><div class="role">Senior Consultant</div></div></div>
</section>

<section class="section faq">
  <div class="photo" role="img" aria-label="Doctor in a white shirt standing in a clinic"></div>
  <h2>QUESTION &amp; ANSWERS</h2>
  <p>We are ready to answer all your queries. Please visit FAQ page. If you have any other questions in your mind then call us</p>
  <div class="btn-outline" style="left:218px;top:268px;width:132px">Read all FAQ's</div>
</section>

<section class="section news">
  <h2>LATEST NEWS</h2>
  <article class="card featured" style="left:118px">
    <span class="ring"></span>
    <div class="meta">John Doe &nbsp;&nbsp; February 25, 2019</div>
    <div class="ftitle">Lorem ipsum dolor sit amet elit dor eget libero vitae</div>
    <div class="excerpt">Lorem ipsum dolor sit amet risus sed... / Read More /</div>
  </article>
  <article class="card" style="left:446px">
    <div class="photo" role="img" aria-label="Senior couple smiling at home"></div>
    <div class="title">Lorem ipsum dolor sit amet elit dor eget libero vitae</div>
  </article>
  <article class="card" style="left:782px">
    <div class="photo" role="img" aria-label="Senior couple smiling at home"></div>
    <div class="title">Lorem ipsum dolor sit amet elit dor eget libero vitae</div>
  </article>
</section>

<section class="section newsletter">
  <h2>SUBSCRIBE OUR NEWSLETTER</h2>
  <div class="sub">Subscribe to our newsletter and never miss the latest news.</div>
  <div class="input" style="left:146px">Name</div>
  <div class="input" style="left:479px">Email</div>
  <div class="send">SUBSCRIBE</div>
</section>

<footer class="section footer">
  <div class="fbrand"><i></i><span>BLUECREST<br>WELLNESS GROUP</span></div>
  <p class="about" style="top:125px">Lorem ipsum dolor sit amet, consectetur adipiscing elit. Ut diam justo, ultricies at purus quis, ultricies ornare orci. Integer laoreet</p>
  <p class="about" style="top:212px">finibus mi. Pellentesque tincidunt eget libero vitae pellentesque. Aliquam interdum risus sed neque molestie, sit amet venenatis nisi</p>
  <h4 style="left:508px">GET TO KNOW US</h4>
  <ul style="left:508px"><li>Home</li><li>About</li><li>Appoinment</li><li>Opioid reduction</li><li>Faq</li><li>Blog</li><li>Contact</li></ul>
  <h4 style="left:710px">FOLLOW</h4>
  <ul class="social" style="left:710px"><li>Community Page</li><li>News Feed</li></ul>
  <h4 style="left:890px">CONTACT</h4>
  <ul style="left:890px"><li>45 Willow Bend Road</li><li>Maple Grove</li><li>+00 222 480 36</li><li>info@bluecrestwellness.com</li></ul>
  <div class="copy">Copyright 2019 © Bluecrest Wellness Group. All rights reserved.</div>
</footer>

</body>
</html>
```